New Bicycle shop business card

Hi!
I'm looking for a business card for my new proffesional bike mechanics shop. This shop is only for fixing broken bikes and not selling bikes.
Peferbly a modern and sleek and modern design.
Colors: black, grey, red, white
Information:
Name: Rijwielwerkplaats Vanhoutem
Shop owner: Bart Vanhoutem & Sanne Maertens
Website: www.rijwielwerkplaats-vanhoutem.be
Email: info@rijwielwerkplaats-vanhoutem.be
Phone number: +32471902386
Street adres: Kerkweg 64
9970 Oostmoere
Slogan/shop information: Herstellingen van alle merken.
Logo: see files.
Target Market(s)
People who seek a mechanic to fix or upgrade their bikes.
Contact Information for Business Card
Information:
Website: info@rijwielwerkplaats-vanhoutem.be
9970 Oostmoere
Logo: see files.

```html
<!DOCTYPE html>
<html lang="nl">
<head>
<meta charset="utf-8">
<title>Rijwielwerkplaats Vanhoutem – visitekaartje</title>
<link rel="stylesheet" href="https://fonts.googleapis.com/css2?family=Open+Sans:wght@400;600;700;800&display=swap">
<style>
  :root {
    --red: #e8264a;
    --black: #0d0d0f;
    --ink: #222226;
    --grey: #9a9ca0;
    --white: #ffffff;
    --backdrop: #2a2d31;
  }
  * { box-sizing: border-box; margin: 0; padding: 0; }
  html, body {
    width: 1200px; height: 900px; overflow: hidden;
    background: var(--backdrop);
    font-family: "Open Sans", Arial, sans-serif;
  }
  .stage {
    position: relative; width: 1200px; height: 900px;
    display: flex; align-items: center; justify-content: center; gap: 60px;
  }
  .card {
    position: relative; width: 520px; height: 336px;
    border-radius: 22px; overflow: hidden;
    box-shadow: 0 18px 40px rgba(0,0,0,.45);
  }

  /* Front */
  .card--front { background: var(--white); }
  .owners-band {
    position: absolute; left: 0; top: 0; width: 100%; height: 84px;
    background: var(--red); color: var(--white);
    padding: 18px 26px 0;
  }
  .owners-band__names {
    font-size: 22px; font-weight: 700; letter-spacing: -.3px;
    line-height: 1.1; white-space: nowrap;
  }
  .owners-band__role { font-size: 10px; font-weight: 700; letter-spacing: .3px; margin-top: 4px; }
  .contact-list {
    position: absolute; left: 26px; top: 104px; list-style: none;
    color: var(--ink); font-size: 14.5px; line-height: 1;
  }
  .contact-list li { display: flex; align-items: center; gap: 10px; height: 30px; white-space: nowrap; }
  .contact-list svg { width: 15px; height: 15px; flex: none; fill: var(--red); }
  .front-mark {
    position: absolute; right: 26px; bottom: 62px;
    display: flex; align-items: center; gap: 10px;
    color: var(--ink); font-size: 13px; font-weight: 700;
    line-height: 1.2; text-align: left;
  }
  .front-mark__square { width: 22px; height: 22px; background: var(--red); flex: none; }
  .slogan-strip {
    position: absolute; left: 0; bottom: 0; width: 100%; height: 42px;
    background: var(--black); color: var(--white);
    font-size: 15px; display: flex; align-items: center; padding-left: 26px;
  }

  /* Back */
  .card--back {
    background: var(--black);
    display: flex; align-items: center; justify-content: center; gap: 14px;
  }
  .back-mark__square { width: 26px; height: 26px; background: var(--red); flex: none; }
  .back-mark__name {
    color: var(--white); font-size: 24px; font-weight: 800;
    letter-spacing: .5px; text-transform: uppercase; line-height: 1.15;
  }
</style>
</head>
<body>
<main class="stage">
  <section class="card card--front" aria-label="Voorzijde visitekaartje">
    <header class="owners-band">
      <p class="owners-band__names">BART VANHOUTEM &amp; SANNE MAERTENS</p>
      <p class="owners-band__role">OWNERS</p>
    </header>

    <ul class="contact-list">
      <li>
        <svg viewBox="0 0 24 24" aria-hidden="true"><path d="M6.6 10.8a15.1 15.1 0 0 0 6.6 6.6l2.2-2.2a1 1 0 0 1 1-.25 11.4 11.4 0 0 0 3.6.57 1 1 0 0 1 1 1V20a1 1 0 0 1-1 1A17 17 0 0 1 3 4a1 1 0 0 1 1-1h3.5a1 1 0 0 1 1 1c0 1.25.2 2.45.57 3.57a1 1 0 0 1-.25 1z"/></svg>
        +32 47 19 02 386
      </li>
      <li>
        <svg viewBox="0 0 24 24" aria-hidden="true"><path d="M2 5h20v14H2z M4 7v.5l8 5.5 8-5.5V7l-8 5.5z" fill-rule="evenodd"/></svg>
        www.rijwielwerkplaats-vanhoutem.be
      </li>
      <li>
        <svg viewBox="0 0 24 24" aria-hidden="true"><path d="M12 2a10 10 0 1 0 0 20 10 10 0 0 0 0-20zm6.9 9h-3a15 15 0 0 0-1.3-5.6A8 8 0 0 1 18.9 11zM12 4.1c.9 1.2 1.7 3.6 1.9 6.9h-3.8c.2-3.3 1-5.7 1.9-6.9zM9.4 5.4A15 15 0 0 0 8.1 11h-3a8 8 0 0 1 4.3-5.6zM5.1 13h3a15 15 0 0 0 1.3 5.6A8 8 0 0 1 5.1 13zm6.9 6.9c-.9-1.2-1.7-3.6-1.9-6.9h3.8c-.2 3.3-1 5.7-1.9 6.9zm2.6-1.3a15 15 0 0 0 1.3-5.6h3a8 8 0 0 1-4.3 5.6z"/></svg>
        info@rijwielwerkplaats-vanhoutem.be
      </li>
      <li>
        <svg viewBox="0 0 24 24" aria-hidden="true"><path d="M12 2a7 7 0 0 0-7 7c0 5 7 13 7 13s7-8 7-13a7 7 0 0 0-7-7zm0 9.5a2.5 2.5 0 1 1 0-5 2.5 2.5 0 0 1 0 5z"/></svg>
        Kerkweg 64, 9970 Oostmoere
      </li>
    </ul>

    <div class="front-mark">
      <span class="front-mark__square" aria-hidden="true"></span>
      <span>Rijwielwerkplaats<br>Vanhoutem</span>
    </div>

    <footer class="slogan-strip">Herstellingen van alle merken</footer>
  </section>

  <section class="card card--back" aria-label="Achterzijde visitekaartje">
    <span class="back-mark__square" aria-hidden="true"></span>
    <p class="back-mark__name">Rijwielwerkplaats<br>Vanhoutem</p>
  </section>
</main>
</body>
</html>
```